The Artist is "Vadrel" and the title of the project is .Z7 I need front and back cover ...

The front cover will be the 2 bullets, instead of the "38 spl" I want it to say Vadrel. Instead of the "HJV" I want it to say .Z7.. the 2 parenthesis looking marks can stay. I want this to look as natural as possible. Like it came from the factory with those words engraved. I was the bullets to keep their same gritty dirty look, along with a clean white background. Very simple. The back cover will be either an enclosed picture of a single bullet hole and the track listing, I will submit the pictures. White is the theme. If the grey metal hole picture is used I want to to be made white with the tracklisting on the background. If another type is used I would like the tracklisting INSIDE the bullet hole. I want the font to look serious and not cartoonish. Right now my tracklisting is kind of changing, so if the artist would be willing to work with me that would be great.
Rap/Hip hop

```html
<!DOCTYPE html>
<html lang="en">
<head>
<meta charset="utf-8">
<title>Vadrel — .Z7 — Back Cover</title>
<link rel="stylesheet" href="https://fonts.googleapis.com/css2?family=Arimo:wght@700&display=swap">
<style>
  :root {
    --paper: #c8c8c6;
    --paper-light: #e6e6e4;
    --paper-shade: #bdbdbb;
    --ink: #121212;
    --hole-dark: #0b0b0b;
    --hole-rim: #9a9a98;
    --hole-edge: #ededeb;
  }
  html, body {
    margin: 0;
    padding: 0;
    width: 1200px;
    height: 1200px;
    overflow: hidden;
  }
  .back-cover {
    position: relative;
    width: 1200px;
    height: 1200px;
    background:
      radial-gradient(ellipse 420px 260px at 1150px 20px, var(--paper-light), transparent 70%),
      linear-gradient(160deg, var(--paper) 0%, var(--paper) 55%, var(--paper-shade) 100%);
    overflow: hidden;
  }
  .tracklist {
    position: absolute;
    left: 133px;
    top: 144px;
    margin: 0;
    padding: 0;
    list-style: none;
    font-family: "Arimo", Arial, sans-serif;
    font-weight: 700;
    font-size: 27px;
    line-height: 48.67px;
    letter-spacing: 0.14em;
    color: var(--ink);
    white-space: nowrap;
  }
  .bullet-hole {
    position: absolute;
    left: 700px;
    top: 420px;
    width: 310px;
    height: 310px;
  }
</style>
</head>
<body>
  <main class="back-cover">
    <ol class="tracklist">
      <li>1. He Chose to die</li>
      <li>2. Grandpa</li>
      <li>3. Should've told em</li>
      <li>4. P.O.T.R</li>
      <li>5. Lookin at me</li>
      <li>6. My plea</li>
      <li>7. Tomorrow never comes</li>
      <li>8. Temptation</li>
      <li>9. When Im from Ft. Calloway</li>
      <li>10. Rest up</li>
      <li>11. 8:30am</li>
      <li>12. High</li>
      <li>13. Noah</li>
      <li>14. Right Now Pt.1</li>
      <li>15. Shut up!</li>
      <li>16. For Love</li>
      <li>17. Yes</li>
      <li>18. Breathing</li>
      <li>19. Beautiful</li>
    </ol>

    <svg class="bullet-hole" viewBox="0 0 310 310" role="img" aria-label="Photograph of a single bullet hole punched through grey metal, torn bright edges around a dark opening">
      <defs>
        <radialGradient id="holeShade" cx="50%" cy="50%" r="50%">
          <stop offset="0%" stop-color="var(--hole-dark)"/>
          <stop offset="52%" stop-color="var(--hole-dark)"/>
          <stop offset="60%" stop-color="var(--hole-rim)"/>
          <stop offset="82%" stop-color="var(--hole-edge)"/>
          <stop offset="100%" stop-color="var(--paper)" stop-opacity="0"/>
        </radialGradient>
      </defs>
      <circle cx="155" cy="155" r="155" fill="url(#holeShade)"/>
    </svg>
  </main>
</body>
</html>
```